Re-design of our website - Property Development Company

Our current website is now old and stale. We are looking for a Wordpress design for a new website. Our company is a property development and property investment company. We have different projects that are under construction and have completed a number also. We would like to showcase these projects as individual pages. The projects are located all over the east coast of Australia and a mixture of retail, industrial, residential subdivsions. In the near future we are hoping to start a small property funds management division as well.

Current website is www.korvanith.com.au

We are wanting you to design a page for the each of following (total of 3 pages):
- Home page
- Project page (which will be used to showcase each development project). There are 4 active projects that we currently own and a number of completed projects.
- Information page (which will be used for about us, contact us, management etc.)

Feel free to go out of the box and wow us. We are open to new ideas.
Updates

Reason: Hi I am going on annual leave for a week being 17-21 Feb so wont be able to comment on anyones design so I have given you an extra week and a bit to finish off your 3 pages. Thanks for the designs so far, they are looking good.

Target Market(s)

It will be used by business professionals researching our company including:
- current investors
- new investors
- consultants (architects, builders, town planners, council, real estate managers/agents, engineers etc.)
- Bank lenders

We want these people to think yes we want to work with this company, they look like they are exceptional at what they do, professional, highly capable.

Industry/Entity Type

Investment

Requirements
Must have
• Our Logo. Files attached. This can be modified if you think it needs to be improved.
Nice to have
• We like clean looking websites.
• We will have some professional photographs taken of our current property developments once they are completed - two shopping centres that will be our signature developments to date. For the time being I have uploaded some aerial photographs on one of our projects under construction and also some nice photos of one of our completed developments. This should help with designing the project page.
Should not have
• We don't like busy websites with too much going on and you don't know what to look at.

```html
<!DOCTYPE html>
<html lang="en">
<head>
<meta charset="utf-8">
<title>Korvanith Partners – Home</title>
<link rel="stylesheet" href="https://fonts.googleapis.com/css2?family=PT+Sans:wght@400;700&display=swap">
<style>
:root{
  --page-bg:#d5d5d5;
  --sheet:#ffffff;
  --footer-bg:#d9d9d9;
  --footer-strip:#3a3a3a;
  --ink:#222222;
  --body-text:#3f3f3f;
  --muted:#a9a9a9;
  --nav-active:#2f8ee0;
  --field-line:#d8d8d8;
  --brand:#1f7fd6;
}
*{box-sizing:border-box;margin:0;padding:0}
html,body{width:723px;height:1200px;overflow:hidden}
body{position:relative;background:var(--page-bg);font-family:"PT Sans",Arial,sans-serif;color:var(--body-text)}
.sheet{position:absolute;left:28px;top:0;width:667px;height:984px;background:var(--sheet)}
.abs{position:absolute}

/* header */
.brand{left:70px;top:20px;display:flex;align-items:center;gap:7px;font-size:17px;font-weight:700;color:var(--brand)}
.brand-mark{width:14px;height:14px;background:var(--brand)}
.nav{top:38px;font-size:11px;color:var(--muted);display:flex}
.nav a{position:absolute;color:var(--muted);text-decoration:none;white-space:nowrap}
.nav a.is-active{color:var(--nav-active)}

.hero{left:71px;top:115px;width:581px;height:85px;background:linear-gradient(90deg,#3b3b3b 0%,#e9d55a 12%,#ecd657 35%,#c9c9c4 55%,#d8cfa0 70%,#a9a7a2 85%,#2c2c2c 100%)}

.heading{font-size:14px;font-weight:400;color:var(--ink)}

/* about */
.about{left:75px;top:270px;width:383px;font-size:11px;line-height:16.7px;text-align:justify;color:var(--body-text)}
.about-photo{float:left;width:140px;height:124px;margin:2px 15px 4px 0;background:radial-gradient(circle at 60% 50%,#3a3a3a 0%,#8d8d8d 30%,#e9e9e9 70%,#f5f5f5 100%)}
.about p{margin:0}

/* management */
.team-photo{width:72px;height:72px;background:linear-gradient(160deg,#8fb6d8,#c79d85 55%,#7aa1c4)}
.team-name{font-size:9.5px;line-height:19px;color:var(--ink);width:92px}
.team-name span{display:block;line-height:13px}

/* form */
.field{left:78px;width:148px;height:30px;border:1.5px solid var(--field-line);font-size:13px;color:#c4c4c4;padding:6px 10px}
.field-message{height:159px;width:334px}
.form-action{font-size:13px;color:var(--ink)}

.map{left:483px;top:629px;width:172px;height:173px;background:linear-gradient(135deg,#ece4c6,#e0dac4 50%,#cfd9c0 80%,#e6e1cd)}
.contact-lines{left:482px;top:829px;font-size:9px;line-height:19.3px;color:var(--body-text)}

/* footer */
.footer{left:30px;top:984px;width:664px;height:211px;background:linear-gradient(170deg,#dadada,#cfcfcf 60%,#d8d8d8)}
.footer-strip{left:30px;top:1195px;width:664px;height:5px;background:var(--footer-strip)}
.footer-heading{font-size:22px;font-weight:400;color:#2e2e2e}
.thumb{width:46px;height:37px}
.t1{background:linear-gradient(160deg,#4b7fd0,#cc3a2f 60%,#e9e2dc)}
.t2{background:linear-gradient(160deg,#b56a5f,#c94a3a 50%,#7a6a5e)}
.t3{background:linear-gradient(160deg,#8fb7e0,#e0c65a 50%,#8b8678)}
.t4{background:linear-gradient(160deg,#6d9ed9,#d9472f 55%,#e8e1d7)}
.t5{background:linear-gradient(160deg,#a7c5e6,#c2634b 50%,#9a8d7a)}
.t6{background:linear-gradient(160deg,#5c5a4e,#a8a89c 50%,#3e3d36)}
.footer-about{left:286px;top:1039px;width:162px;font-size:8.2px;line-height:14.3px;color:#333}
.read-more{left:293px;top:1129px;font-size:10.5px;color:#2a2a2a}
.news-field{left:482px;width:157px;height:21px;background:#e9e9e9;border:1px solid #c6c6c6;font-size:10px;color:#8a8a8a;padding:3px 16px}
.news-submit{left:482px;top:1115px;width:57px;height:17px;background:#efefef;border:1px solid #c6c6c6;font-size:10px;color:#2a2a2a;text-align:center;line-height:15px}
.copyright{left:70px;top:1170px;font-size:9.5px;color:#333}
.to-top{left:702px;top:1183px}
</style>
</head>
<body>
<div class="sheet"></div>

<div class="abs brand"><span class="brand-mark"></span>Korvanith</div>

<nav class="abs nav">
  <a class="is-active" href="#" style="left:461px">Home</a>
  <a href="#" style="left:501px">Project</a>
  <a href="#" style="left:549px">Information</a>
  <a href="#" style="left:618px">Contact</a>
</nav>

<div class="abs hero" role="img" aria-label="Street view of a yellow and grey retail centre facade"></div>

<h2 class="abs heading" style="left:78px;top:234px">About Us</h2>
<div class="abs about">
  <div class="about-photo" role="img" aria-label="Black chess king in front of blurred pawns"></div>
  <p>Having started operations in 2001, Korvanith Partners is an established “value add” property group with a focus on property development.</p>
  <p>Korvanith Partners is an opportunistic total return investor / developer with the proven capability to successfully identify, acquire, manage and deliver property projects that are anticipated to deliver strong returns to our group and partners.</p>
  <p>Through the projects we have created and participated in over the years, Korvanith Partners has refined substantial skill sets in the areas of bulky goods, retail, industrial and commercial development.</p>
  <p>Our next wave of projects have been acquired during 2010 and 2011 and include a number of retail and residential developments in growth locations across the eastern seaboard from as far north as Mackay in Queensland down to Launceston in Tasmania.</p>
</div>

<h2 class="abs heading" style="left:484px;top:234px">Mangement</h2>
<div class="abs team-photo" style="left:484px;top:274px" role="img" aria-label="Portrait of Daniel Ferrow"></div>
<div class="abs team-photo" style="left:581px;top:274px" role="img" aria-label="Portrait of Alan Pritchard"></div>
<div class="abs team-name" style="left:486px;top:350px"><span>Daniel Ferrow</span>Managing Director / Principal</div>
<div class="abs team-name" style="left:583px;top:350px"><span>Alan Pritchard</span>Managing Director / Principal</div>
<div class="abs team-photo" style="left:484px;top:410px" role="img" aria-label="Portrait of Kenji Morau"></div>
<div class="abs team-photo" style="left:581px;top:410px" role="img" aria-label="Portrait of Daniel Ferrow"></div>
<div class="abs team-name" style="left:486px;top:486px"><span>Kenji Morau</span>Director / Principal</div>
<div class="abs team-name" style="left:583px;top:486px"><span>Daniel Ferrow</span>Managing Director / Principal</div>

<h2 class="abs heading" style="left:78px;top:565px">Get in touch</h2>
<div class="abs field" style="top:629px">Name</div>
<div class="abs field" style="top:676px">E-mail</div>
<div class="abs field" style="top:723px">Phone</div>
<div class="abs field field-message" style="top:770px">Phone</div>
<div class="abs form-action" style="left:298px;top:942px">Clear<small>→</small></div>
<div class="abs form-action" style="left:371px;top:942px">Submit<small>→</small></div>

<h2 class="abs heading" style="left:484px;top:565px">Contact info</h2>
<div class="abs map" role="img" aria-label="Street map showing the office location"></div>
<div class="abs contact-lines">
  Level 9, Harbourline House<br>
  14 Wexley Street,SYDNEY<br>
  Freephone:02 8000 4172<br>
  Telephone:02 9311 0482<br>
  FAX: 02 9311 0499<br>
  E-mail: daniel@korvanith.com.au
</div>

<div class="abs footer"></div>
<div class="abs footer-strip"></div>

<h3 class="abs footer-heading" style="left:70px;top:1004px">Gallery</h3>
<div class="abs thumb t1" style="left:70px;top:1039px" role="img" aria-label="Retail centre with red umbrellas"></div>
<div class="abs thumb t2" style="left:139px;top:1039px" role="img" aria-label="Shopfront walkway"></div>
<div class="abs thumb t3" style="left:208px;top:1039px" role="img" aria-label="Yellow retail facade"></div>
<div class="abs thumb t4" style="left:70px;top:1095px" role="img" aria-label="Red and white storefront"></div>
<div class="abs thumb t5" style="left:139px;top:1095px" role="img" aria-label="Shopping centre exterior"></div>
<div class="abs thumb t6" style="left:208px;top:1095px" role="img" aria-label="Aerial view of construction site"></div>

<h3 class="abs footer-heading" style="left:283px;top:1004px">About us</h3>
<p class="abs footer-about">Praesent vestibulm mostie lacus. Aeneanmmy hendrerit mauris. Phases po. Fusce suscipit var mi. Cum sociis natoque pentis et mais dis parttones nastur rid mus. Nulla dui. Fusce feu giat malesuaddio. Morbi nunc.</p>
<div class="abs read-more">Read More ▸</div>

<h3 class="abs footer-heading" style="left:483px;top:1004px">Newsletter</h3>
<div class="abs news-field" style="top:1052px">Name</div>
<div class="abs news-field" style="top:1082px">Email</div>
<div class="abs news-submit">Submit</div>

<div class="abs copyright">Korvanith © 2014 All Right Reserved.</div>

<svg class="abs to-top" width="12" height="12" viewBox="0 0 12 12" aria-hidden="true">
  <circle cx="6" cy="6" r="5.5" fill="#f2f2f2" stroke="#bdbdbd"/>
  <path d="M3.8 7 L6 4.8 L8.2 7" fill="none" stroke="#666" stroke-width="1"/>
</svg>
</body>
</html>
```